Business card and stationery for startup company
Marla Quenby & Associates
Business card and stationery for startup company - Corporate Services
Creative Brief
Professional
Marla Quenby
PO Box 382 Northville, MI 48193
marlaequenby@postvane.com
Concepts
Business Cards and Stationery for Background Check Company
Business Cards and Stationery for new compliance company.

```html
<!DOCTYPE html>
<html lang="en">
<head>
<meta charset="utf-8">
<title>Marla Quenby &amp; Associates — Stationery</title>
<link href="https://fonts.googleapis.com/css2?family=Cinzel:wght@500&family=Open+Sans:wght@400;600&display=swap" rel="stylesheet">
<style>
:root{
  --stage:#5e5f61;
  --paper:#ffffff;
  --navy:#1d3f7a;
  --blue:#1f5fae;
  --brown:#5a3a1e;
  --ink:#333;
  --rule:#9a9a9a;
  --label:#d8d8d8;
}
*{margin:0;padding:0;box-sizing:border-box}
html,body{width:1200px;height:511px;overflow:hidden}
body{background:var(--stage);font-family:"Open Sans",sans-serif;position:relative}
.sheet{position:absolute;background:var(--paper);overflow:hidden;box-shadow:0 2px 6px rgba(0,0,0,.35)}
.letterhead{left:53px;top:19px;width:240px;height:401px}
.fax{left:324px;top:19px;width:240px;height:401px}
.brand{position:absolute;display:flex;align-items:center;gap:5px}
.brand-dot{width:12px;height:12px;border-radius:50%;background:var(--blue);flex:none}
.brand-name{font-family:"Cinzel",serif;font-weight:500;color:var(--navy);font-size:9px;white-space:nowrap}
.brand-sub{position:absolute;font-size:4px;color:var(--navy);letter-spacing:.3px;white-space:nowrap}
.sheet .brand{left:70px;top:12px}
.sheet .brand-sub{left:87px;top:27px}
.band{position:absolute;left:0;bottom:0;width:100%}
.footer-text{position:absolute;right:8px;bottom:5px;font-size:3.6px;color:#fff;white-space:nowrap}
.option-label{position:absolute;top:441px;font-size:10px;color:var(--label);width:240px;text-align:center}
.fax-title{position:absolute;left:14px;top:48px;font-size:15px;color:var(--ink);letter-spacing:1px}
.fax-fields{position:absolute;left:14px;top:74px;width:212px;display:grid;grid-template-columns:1fr 1fr;column-gap:10px;row-gap:8px}
.field{font-size:4px;color:#555;border-bottom:.6px solid var(--rule);padding-bottom:1px}
.fax-checks{position:absolute;left:14px;top:123px;display:flex;gap:9px}
.check{font-size:4px;color:#555;display:flex;align-items:center;gap:2px}
.check::before{content:"";width:4px;height:4px;border:.6px solid #777}
.envelope{position:absolute;width:247px;height:110px;background:var(--paper);overflow:hidden;box-shadow:0 2px 5px rgba(0,0,0,.35)}
.envelope-back{left:629px;top:19px}
.envelope-mid{left:629px;top:90px;height:90px}
.envelope-front{left:629px;top:150px}
.envelope .brand{left:12px;top:10px}
.envelope .brand-dot{width:9px;height:9px}
.envelope .brand-name{font-size:7px}
.envelope .brand-sub{left:26px;top:22px}
.return-address{position:absolute;left:26px;top:28px;font-size:3.6px;color:#555}
.card{position:absolute;width:120px;height:58px;background:var(--paper);overflow:hidden;box-shadow:0 2px 5px rgba(0,0,0,.35)}
.card .brand{left:8px;top:8px}
.card .brand-dot{width:7px;height:7px}
.card .brand-name{font-size:5.5px}
.card .brand-sub{left:20px;top:17px;font-size:3px}
.card-person{position:absolute;left:20px;top:24px;font-size:3.6px;color:var(--ink);line-height:1.4}
</style>
</head>
<body>

<section class="sheet letterhead">
  <div class="brand"><span class="brand-dot"></span><span class="brand-name">Marla Quenby &amp; Associates</span></div>
  <div class="brand-sub">Compliance and Background Services</div>
  <svg class="band" viewBox="0 0 240 40" height="40" aria-hidden="true">
    <path d="M0 12 Q120 0 240 14 V40 H0Z" fill="var(--brown)"/>
    <path d="M0 16 Q120 4 240 18 V40 H0Z" fill="var(--blue)"/>
  </svg>
  <div class="footer-text">PO Box 382 Northville, MI 48193 · marlaequenby@postvane.com</div>
</section>
<div class="option-label" style="left:53px">Option 1</div>

<section class="sheet fax">
  <div class="brand"><span class="brand-dot"></span><span class="brand-name">Marla Quenby &amp; Associates</span></div>
  <div class="brand-sub">Compliance and Background Services</div>
  <div class="fax-title">FAX</div>
  <div class="fax-fields">
    <div class="field">To:</div><div class="field">From:</div>
    <div class="field">Fax:</div><div class="field">Pages:</div>
    <div class="field">Phone:</div><div class="field">Date:</div>
    <div class="field">Re:</div><div class="field">CC:</div>
  </div>
  <div class="fax-checks">
    <span class="check">Urgent</span><span class="check">For Review</span><span class="check">Please Comment</span><span class="check">Please Reply</span><span class="check">Please Recycle</span>
  </div>
  <svg class="band" viewBox="0 0 240 40" height="40" aria-hidden="true">
    <path d="M0 12 Q120 0 240 14 V40 H0Z" fill="var(--brown)"/>
    <path d="M0 16 Q120 4 240 18 V40 H0Z" fill="var(--blue)"/>
  </svg>
  <div class="footer-text">PO Box 382 Northville, MI 48193 · marlaequenby@postvane.com</div>
</section>
<div class="option-label" style="left:324px">Option 2</div>

<section class="envelope envelope-back">
  <svg width="247" height="110" viewBox="0 0 247 110" aria-hidden="true">
    <path d="M0 0 H247 V62 Q124 40 0 68Z" fill="var(--blue)"/>
    <path d="M0 68 Q124 40 247 62" fill="none" stroke="var(--brown)" stroke-width="3"/>
  </svg>
</section>

<section class="envelope envelope-mid">
  <svg width="247" height="90" viewBox="0 0 247 90" aria-hidden="true">
    <path d="M0 0 L124 40 L247 0" fill="none" stroke="#ccc" stroke-width=".8"/>
  </svg>
</section>

<section class="envelope envelope-front">
  <div class="brand"><span class="brand-dot"></span><span class="brand-name">Marla Quenby &amp; Associates</span></div>
  <div class="brand-sub">Compliance and Background Services</div>
  <div class="return-address">PO Box 382 Northville, MI 48193</div>
  <svg class="band" viewBox="0 0 247 26" height="26" aria-hidden="true">
    <path d="M60 26 Q160 4 247 2 V26Z" fill="var(--brown)"/>
    <path d="M90 26 Q170 10 247 8 V26Z" fill="var(--blue)"/>
  </svg>
</section>

<section class="card" style="left:636px;top:276px">
  <div class="brand"><span class="brand-dot"></span><span class="brand-name">Marla Quenby &amp; Associates</span></div>
  <div class="brand-sub">Compliance and Background Services</div>
  <div class="card-person">Marla Quenby · Principal<br>marlaequenby@postvane.com</div>
  <svg class="band" viewBox="0 0 120 14" height="14" aria-hidden="true">
    <path d="M0 6 Q60 0 120 4 V14 H0Z" fill="var(--brown)"/>
    <path d="M0 8 Q60 2 120 6 V14 H0Z" fill="var(--blue)"/>
  </svg>
</section>

<section class="card" style="left:780px;top:276px">
  <div class="brand"><span class="brand-dot"></span><span class="brand-name">Marla Quenby &amp; Associates</span></div>
  <div class="brand-sub">Compliance and Background Services</div>
  <div class="card-person">Marla Quenby · Principal<br>marlaequenby@postvane.com</div>
  <svg class="band" viewBox="0 0 120 18" height="18" aria-hidden="true">
    <path d="M0 8 Q60 0 120 5 V18 H0Z" fill="var(--brown)"/>
    <path d="M0 11 Q60 3 120 8 V18 H0Z" fill="var(--blue)"/>
  </svg>
</section>

<section class="card" style="left:636px;top:348px">
  <div class="brand"><span class="brand-dot"></span><span class="brand-name">Marla Quenby &amp; Associates</span></div>
  <div class="brand-sub">Compliance and Background Services</div>
  <div class="card-person">Marla Quenby · Principal<br>marlaequenby@postvane.com</div>
  <svg class="band" viewBox="0 0 120 16" height="16" aria-hidden="true">
    <path d="M0 6 Q60 0 120 4 V16 H0Z" fill="var(--brown)"/>
  </svg>
</section>

<section class="card" style="left:780px;top:348px">
  <div class="brand"><span class="brand-dot"></span><span class="brand-name">Marla Quenby &amp; Associates</span></div>
  <div class="brand-sub">Compliance and Background Services</div>
  <div class="card-person">Marla Quenby · Principal<br>marlaequenby@postvane.com</div>
  <svg class="band" viewBox="0 0 120 22" height="22" aria-hidden="true">
    <path d="M0 8 Q60 0 120 4 V22 H0Z" fill="var(--brown)"/>
  </svg>
</section>

</body>
</html>
```